Label Design for a New Alcoholized Root Beer

Create a design for a new alcoholized root beer. This is a new product category in the USA growing very rapidly. Root Beer is a popular flavor of Cola, but recently, beer manufacturers have added alcohol to it and have created a new product that has gained traction on the market at a tremendous rate.

Root Beer is vintage product that has been around for a hundred years. Consumers of this product are mostly male between the age of 30 to 45. They purchase this product for its nostalgia and vintage look and taste.

This product will be in a standard 355 mL brown bottle.

It is 5.9% abv.

The name of the product is ''Osric's Hard Root Beer''.

We have uploaded some pictures of traditional root beers to give you an idea of the feel we want our product to have and also, the bottle the product will be filled in.

Target Market(s)

Consumers are male 30-45, same market as craft beer consumers

Industry/Entity Type

Product

Requirements
Must have
• Design must have a vintage feel to it

```html
<!DOCTYPE html>
<html lang="en">
<head>
<meta charset="UTF-8">
<title>Osric's Hard Root Beer – Label</title>
<link href="https://fonts.googleapis.com/css2?family=Rye&family=Merriweather:wght@700&display=swap" rel="stylesheet">
<style>
  :root {
    --backdrop: #161414;
    --label-red: #d12a26;
    --label-red-deep: #8e1712;
    --label-navy: #2b2c5e;
    --gold: #e8b54a;
    --gold-light: #f6cf6a;
    --gold-dark: #a8711f;
    --ink: #2a1a0e;
    --ribbon-light: #f0a030;
    --ribbon-dark: #b8521a;
    --ribbon-tail: #c9641f;
    --oval-light: #ec7a2c;
    --oval-mid: #c8401c;
    --oval-dark: #7e1a10;
    --oval-shadow: #4a2a18;
    --white: #ffffff;
  }
  html, body {
    margin: 0;
    padding: 0;
    width: 1000px;
    height: 1200px;
    overflow: hidden;
    background: var(--backdrop);
  }
  .canvas {
    width: 1000px;
    height: 1200px;
    display: flex;
    align-items: center;
    justify-content: center;
  }
  .label {
    width: 520px;
    height: 900px;
    display: block;
  }
  .label-title {
    font-family: "Rye", serif;
    fill: var(--gold);
    stroke: var(--ink);
    stroke-width: 3;
    paint-order: stroke;
    text-anchor: middle;
  }
  .label-ribbon-text {
    font-family: "Rye", serif;
    fill: var(--ink);
    text-anchor: middle;
  }
  .label-specs {
    font-family: "Merriweather", serif;
    font-weight: 700;
    fill: var(--white);
    text-anchor: middle;
  }
</style>
</head>
<body>
<main class="canvas">
  <svg class="label" viewBox="0 0 520 900" xmlns="http://www.w3.org/2000/svg" aria-label="Osric's Hard Root Beer bottle label">
    <defs>
      <linearGradient id="portrait-fill" x1="0" y1="0" x2="1" y2="0.4">
        <stop offset="0%" stop-color="var(--oval-dark)"/>
        <stop offset="30%" stop-color="var(--oval-light)"/>
        <stop offset="60%" stop-color="var(--oval-mid)"/>
        <stop offset="100%" stop-color="var(--oval-dark)"/>
      </linearGradient>
      <radialGradient id="portrait-figure" cx="55%" cy="65%" r="45%">
        <stop offset="0%" stop-color="var(--oval-shadow)" stop-opacity="0.75"/>
        <stop offset="100%" stop-color="var(--oval-shadow)" stop-opacity="0"/>
      </radialGradient>
      <radialGradient id="hop-fill" cx="45%" cy="40%" r="60%">
        <stop offset="0%" stop-color="var(--gold-light)"/>
        <stop offset="100%" stop-color="var(--gold-dark)"/>
      </radialGradient>
      <linearGradient id="ribbon-fill" x1="0" y1="0" x2="0" y2="1">
        <stop offset="0%" stop-color="var(--ribbon-light)"/>
        <stop offset="100%" stop-color="var(--ribbon-dark)"/>
      </linearGradient>
      <path id="title-arc" d="M90,128 Q260,88 430,128"/>
    </defs>

    <!-- Label body -->
    <path class="label-border" fill="var(--label-red)"
      d="M44,0 H476 A44,44 0 0 0 520,44 V856 A44,44 0 0 0 476,900 H44 A44,44 0 0 0 0,856 V44 A44,44 0 0 0 44,0 Z"/>
    <path class="label-border-inset" fill="var(--label-red-deep)"
      d="M54,12 H466 A42,42 0 0 0 508,54 V846 A42,42 0 0 0 466,888 H54 A42,42 0 0 0 12,846 V54 A42,42 0 0 0 54,12 Z"/>
    <path class="label-panel" fill="var(--label-navy)"
      d="M58,18 H462 A40,40 0 0 0 502,58 V842 A40,40 0 0 0 462,882 H58 A40,40 0 0 0 18,842 V58 A40,40 0 0 0 58,18 Z"/>

    <!-- Product name -->
    <text class="label-title" font-size="62">
      <textPath href="#title-arc" startOffset="50%">OSRIC'S</textPath>
    </text>
    <text class="label-title" x="260" y="196" font-size="56">HARD</text>

    <!-- Hop ornaments -->
    <ellipse role="img" aria-label="Gold hop leaves ornament, left" cx="80" cy="236" rx="30" ry="36" fill="url(#hop-fill)" opacity="0.9"/>
    <ellipse role="img" aria-label="Gold hop leaves ornament, right" cx="440" cy="236" rx="30" ry="36" fill="url(#hop-fill)" opacity="0.9"/>

    <!-- Portrait oval -->
    <ellipse class="portrait-frame" cx="260" cy="395" rx="230" ry="128" fill="var(--ink)"/>
    <ellipse class="portrait-frame-beads" cx="260" cy="395" rx="224" ry="122" fill="none"
      stroke="var(--gold)" stroke-width="9" stroke-dasharray="2.5 2.5"/>
    <ellipse class="portrait-frame-line" cx="260" cy="395" rx="216" ry="114" fill="none"
      stroke="var(--gold-dark)" stroke-width="2"/>
    <g role="img" aria-label="Vintage illustration of a gentleman in a bowler hat raising a frothy mug of root beer">
      <ellipse cx="260" cy="395" rx="214" ry="112" fill="url(#portrait-fill)"/>
      <ellipse cx="260" cy="395" rx="214" ry="112" fill="url(#portrait-figure)"/>
    </g>

    <!-- Ribbon banner -->
    <path class="ribbon-tail" fill="var(--ribbon-tail)"
      d="M18,552 L82,538 L82,612 L18,618 L44,585 Z"/>
    <path class="ribbon-tail" fill="var(--ribbon-tail)"
      d="M502,552 L438,538 L438,612 L502,618 L476,585 Z"/>
    <path class="ribbon-band" fill="url(#ribbon-fill)" stroke="var(--ink)" stroke-width="1.5"
      d="M66,526 Q260,506 454,526 L454,600 Q260,580 66,600 Z"/>
    <text class="label-ribbon-text" x="260" y="578" font-size="44">ROOT BEER</text>

    <!-- Bottom hop ornament -->
    <ellipse role="img" aria-label="Gold hop cone and leaves ornament" cx="260" cy="672" rx="50" ry="40" fill="url(#hop-fill)" opacity="0.9"/>

    <!-- Specs -->
    <text class="label-specs" x="260" y="772" font-size="26">5.9% abv.</text>
    <text class="label-specs" x="260" y="808" font-size="26">355 mL</text>
  </svg>
</main>
</body>
</html>
```